Flyer for Restaurant/Cafe/Bar Point of Sale System

We require an A5 double-sided flyer for our Point of Sale System.
LANDSCAPE FORMAT. To be provided as .eps .jpg and .pdf
Our website:
http://tilvaro-hub.net/point-of-sale-solution/
FRONT SIDE
Tilvaro Hub Logo
Catchphrase:
More Sales, Additional Revenue, Happier Customers
Tilvaro Hub is a next generation Point of Sale system, which increases revenues up to 26% for restaurants, bars, cafés; and improves customer satisfaction. A digital menu is located on each table and linked to our main ePOS units behind the counters/bars and in your kitchen. Customers can order and pay directly using the table top digital menu, without leaving their seat. How convenient!
We also display background ad images on the screen when not in use, but don't worry, you have full control over the types of image so they compliment the atmosphere. The table top menu also has no sound, and the screens can be easily dimmed or blanked by your customers if they wish.
Website: http://tilvaro-hub.net/
Email: info@tilvaro-hub.net
Phone: +353 87 5902248
REAR SIDE
The following should be presented in two side by side tables.
ESSENTIAL FACTS*:
1. Table top Point Of Sale generates up to 26% increase in revenues for restaurants, bars and cafes.
2. Table top Point of Sale generates up to 10% reduction in table turnaround times for restaurants, bars and cafes.
3. Table top Point of Sale generates increased tips for staff.
4. Almost nine out of 10 people boycott a pub or restaurant in protest against slow service
5. 65% of people want their order taken within 5-10 minutes after being seated
6. 51% of all restaurant complaints are related to slow service.
7. Irish employees lose up to 51.8 million hours per year waiting in queues at lunchtime on weekdays.
WHY TRY TILVARO HUB:
• No more lost sales caused by slow service or inconvenience when ordering.
• Eliminate queues and increase customer satisfaction.
• Increase staff efficiency and tips for staff.
• All hardware provided free of charge.
• No installation fees. Plug and play system.
• Excellent service support.
• Industry average transaction fees.
• 20% ad revenue refund to premises.
• 20% games revenue refund to premises.
• No quibble contract withdrawl during 30 day trial period.
• Fixed €10 per month license fee per premises.
• No license fee during 30 day trial period.
• You have full control over the types of ad images that can display so the images compliment the environment.
• Payment is complete before the order is transmitted to your main ePOS from the table, no 'fake' orders.
• No sound on the devices, they are unobtrusive.
• Dimming and 'Opt-Out' buttons if customers want to blank the screen.
• Premises can switch between table service or click-and-collect.
Everything you do now, you can still do. Table top units are a fantastic additional convenience for customers, at no additional cost, which increases your revenue.
* Based on primary and secondary market research.
Tilvaro Hub Limited is registered in the Republic of Ireland. CRO No.647219.
Resolution: 300 DPI
Full Bleed Size:
213 x 151 mm
2517 x 1783 pixels
Trim Size:
210 x 148 mm
2480 x 1748 pixels

```html
<!DOCTYPE html>
<html lang="en">
<head>
<meta charset="utf-8">
<title>Tilvaro Hub – Point of Sale Flyer</title>
<link rel="stylesheet" href="https://fonts.googleapis.com/css2?family=Didact+Gothic&display=swap">
<style>
  :root {
    --green: #8dc63f;
    --green-dark: #6fa52c;
    --pink: #e2007a;
    --pink-dark: #b0005e;
    --ink: #111111;
    --body-ink: #2a2a2a;
    --paper: #ffffff;
    --paper-edge: #dcdcdc;
    --shadow: #c9c9c9;
  }
  * { margin: 0; padding: 0; box-sizing: border-box; }
  html, body { width: 1200px; height: 846px; overflow: hidden; }
  body {
    font-family: "Didact Gothic", "Century Gothic", sans-serif;
    background: var(--paper);
  }
  .flyer {
    position: relative;
    width: 1200px;
    height: 846px;
    overflow: hidden;
    background: radial-gradient(ellipse at 50% 45%, var(--paper) 45%, var(--paper-edge) 100%);
  }
  .flyer__art { position: absolute; inset: 0; }
  .brand-name {
    font-family: "Didact Gothic", "Century Gothic", sans-serif;
    fill: var(--ink);
  }
  .tagline {
    position: absolute;
    font-size: 35px;
    line-height: 1;
    letter-spacing: -0.5px;
    white-space: nowrap;
  }
  .tagline--sales { left: 180px; top: 291px; color: var(--ink); }
  .tagline--revenue { left: 408px; top: 290px; color: var(--paper); }
  .tagline--customers { left: 760px; top: 287px; color: var(--ink); }
  .copy {
    position: absolute;
    left: 118px;
    width: 964px;
    font-size: 19px;
    line-height: 36.8px;
    text-align: justify;
    text-align-last: left;
  }
  .copy--intro { top: 375px; color: var(--body-ink); }
  .copy--ads { top: 549px; color: var(--pink); }
  .divider {
    position: absolute;
    left: 118px;
    width: 964px;
    height: 4px;
    border-top: 1px solid var(--green);
    border-bottom: 1px solid var(--pink);
    opacity: 0.7;
  }
  .divider--top { top: 534px; }
  .divider--bottom {
    top: 683px;
    border-top-color: var(--pink);
    border-bottom-color: var(--green);
  }
  .contact {
    position: absolute;
    left: 466px;
    top: 702px;
    list-style: none;
    color: var(--pink);
    font-size: 18px;
    line-height: 37px;
  }
</style>
</head>
<body>
  <main class="flyer">
    <svg class="flyer__art" width="1200" height="846" viewBox="0 0 1200 846" aria-hidden="true">
      <!-- green swoosh band, top left -->
      <path d="M0,0 H230 C150,20 110,90 110,160 C110,225 160,262 240,266 H370 L392,310 L370,354 H250 C130,350 40,330 0,296 Z" fill="var(--shadow)"/>
      <path d="M0,0 H216 C140,20 100,90 100,160 C100,225 150,262 232,264 H366 L388,308 L366,350 H240 C125,347 35,328 0,292 Z" fill="var(--green)"/>
      <!-- green arrow, right -->
      <path d="M724,266 H1060 L1084,308 L1060,356 H724 L740,308 Z" fill="var(--shadow)"/>
      <path d="M718,263 H1056 L1080,306 L1056,352 H718 L736,306 Z" fill="var(--green)"/>
      <!-- pink arrow, centre -->
      <path d="M374,266 H720 L742,310 L720,356 H374 L394,310 Z" fill="var(--shadow)"/>
      <path d="M368,263 H714 L736,306 L714,352 H368 L388,306 Z" fill="var(--pink)"/>
      <path d="M368,263 L388,306 L368,352 L376,306 Z" fill="var(--pink-dark)"/>
      <!-- pink chevron, far right -->
      <path d="M1064,262 H1076 L1102,308 L1076,356 H1064 L1088,308 Z" fill="var(--shadow)"/>
      <path d="M1058,260 H1070 L1096,306 L1070,352 H1058 L1082,306 Z" fill="var(--pink)"/>
      <rect x="1038" y="272" width="9" height="9" fill="var(--pink)"/>
      <rect x="1042" y="334" width="9" height="9" fill="var(--pink)"/>
      <!-- brand name -->
      <text class="brand-name" x="236" y="160" font-size="134" textLength="628" lengthAdjust="spacingAndGlyphs">TILVARO</text>
      <text class="brand-name" x="628" y="228" font-size="66" textLength="216" lengthAdjust="spacingAndGlyphs">HUB</text>
    </svg>

    <p class="tagline tagline--sales">More Sales</p>
    <p class="tagline tagline--revenue">Additional Revenue</p>
    <p class="tagline tagline--customers">Happier Customers</p>

    <p class="copy copy--intro">Tilvaro Hub is a next generation Point of Sale system, which increases revenues up to 26% for restaurants, bars, cafés; and improves customer satisfaction. A digital menu is located on each table and linked to our main ePOS units behind the counters/bars and in your kitchen. Customers can order and pay directly using the table top digital menu, without leaving their seat. How convenient!</p>

    <div class="divider divider--top"></div>

    <p class="copy copy--ads">We also display background ad images on the screen when not in use, but don't worry, you have full control over the types of image so they compliment the atmosphere. The table top menu also has no sound, and the screens can be easily dimmed or blanked by your customers if they wish.</p>

    <div class="divider divider--bottom"></div>

    <ul class="contact">
      <li>Website: www.tilvaro-hub.net</li>
      <li>Email: info@tilvaro-hub.net</li>
      <li>Phone: +353 87 5902248</li>
    </ul>
  </main>
</body>
</html>
```